Private launch of Lunet, the smart baby sleep tracker

We need a webpage/website to initiate the Private launch of Lunet, our baby sleep tracker.

Meet Lunet:
Sleep, or rather the lack of sleep, is the one of the most challenging aspect of caring for a newborn in the first year. Recently, phone apps for baby tracking have taken hold. But those continue requiring parents to manually enter sleep and awake time. Sleep-deprived parents need a safe, automatic, accurate and stress-free tracking system. Therefore, we provide an affordable smart wearable to track baby’s sleep based on baby’s vital signs.

Target Market(s)

new parents with infants

Industry/Entity Type

Baby Care

Number of Pages Required

1 page

Font styles to use
Sans Serif

Colors
85cae6
f8ba93

Requirements
Must have
• Lunet baby sleep tracker, demonstration video, payment and ordering information. Introduction of our company "Corvane Tesk Digital".
• Considering the primary targets are sleep-deprived new parents, the webpage should be user-friendly.
Nice to have
• Product rating and reviews

```html
<!DOCTYPE html>
<html lang="en">
<head>
<meta charset="utf-8">
<title>Lunet — Smart Baby Sleep Tracker by Corvane Tesk Digital</title>
<link rel="stylesheet" href="https://fonts.googleapis.com/css2?family=Fredoka:wght@500;600&family=Poppins:ital,wght@0,400;0,500;0,600;1,600&display=swap">
<style>
:root{
  --teal:#6bd5cf;
  --teal-deep:#4fc7c0;
  --orange:#ff8029;
  --sky:#85cae6;
  --sky-soft:#a9cde2;
  --peach:#f8ba93;
  --blush:#f1e4e4;
  --white:#ffffff;
  --ink:#3b3b3b;
  --muted:#555555;
  --footer-ink:#2f5f5c;
}
*{box-sizing:border-box;margin:0;padding:0}
html,body{width:1200px;height:3071px;overflow:hidden}
body{font-family:"Poppins",sans-serif;color:var(--ink);background:var(--teal)}
.section{position:absolute;left:0;width:1200px;overflow:hidden}
.heading{font-family:"Fredoka",sans-serif;font-weight:600}

/* Hero */
.hero{top:0;height:632px;background:var(--teal)}
.branch{position:absolute;top:40px;width:320px;height:60px;background:linear-gradient(90deg,rgba(110,80,70,.35),rgba(60,170,130,.35));border-radius:30px}
.branch-left{left:-10px}
.branch-right{right:-10px}
.brand{position:absolute;top:48px;left:0;width:1200px;display:flex;justify-content:center;align-items:center;gap:12px}
.brand-mark{width:22px;height:22px;border-radius:50%;background:var(--orange)}
.brand-name{font-family:"Fredoka",sans-serif;font-weight:600;font-size:34px;color:var(--white)}
.nav{position:absolute;top:170px;left:0;width:1200px;font-size:19px;color:var(--white)}
.nav a{position:absolute;transform:translateX(-50%);color:inherit;text-decoration:none;white-space:nowrap}
.nav a.is-active{color:#3d6e6b}
.hero-title{position:absolute;left:112px;top:336px;font-size:56px;line-height:60px;color:var(--white)}
.hero-photo{position:absolute;left:650px;top:286px;width:440px;height:346px;border-radius:200px 200px 0 0;background:linear-gradient(160deg,#f6d7c4,#e7b79a 55%,#c78a6a)}
.hero-ring{position:absolute;left:606px;top:308px;width:196px;height:196px;border-radius:50%;border:8px solid var(--peach);background:var(--white)}

/* Feature */
.feature{top:632px;height:549px;background:var(--sky-soft)}
.feature-photo{position:absolute;left:0;top:0;width:720px;height:549px;background:linear-gradient(90deg,#7fb0cc 0%,var(--sky) 55%,rgba(169,205,226,0) 100%)}
.feature-title{position:absolute;left:0;width:1532px;top:116px;text-align:center;font-size:38px;color:var(--white)}
.feature-card{position:absolute;top:198px;width:156px;height:180px;background:var(--white);border-radius:6px;box-shadow:0 4px 10px rgba(0,0,0,.12);text-align:center}
.feature-card svg{margin-top:16px}
.feature-card p{font-weight:600;font-size:16px;line-height:19px;margin-top:6px;color:var(--ink)}
.step-arrow{position:absolute;top:271px;width:32px;height:32px;border-radius:50%;background:var(--white)}

/* How it works */
.how{top:1181px;height:544px;background:linear-gradient(110deg,var(--blush),#f4e8e6 50%,#ecdad6)}
.video{position:absolute;left:113px;top:131px;width:474px;height:284px;border:2px solid var(--orange);border-radius:8px;background:linear-gradient(135deg,#f3f3f3,#dcdcdc 55%,#9fd9d3);overflow:hidden}
.play{position:absolute;left:210px;top:115px;width:54px;height:54px}
.how-title{position:absolute;left:694px;top:122px;font-size:38px;color:var(--orange)}
.how-copy{position:absolute;left:694px;top:178px;width:392px;font-size:15.6px;line-height:23.2px;color:var(--ink)}

/* Products */
.products{top:1725px;height:497px;background:var(--orange)}
.products-title{position:absolute;left:0;width:1200px;top:72px;text-align:center;font-size:40px;color:var(--white)}
.product-card{position:absolute;top:158px;width:225px;height:234px;background:var(--white);border-radius:8px;text-align:center}
.product-year{font-family:"Fredoka",sans-serif;font-weight:600;font-size:27px;color:var(--teal-deep);margin-top:16px}
.product-shot{width:130px;height:48px;border-radius:24px;margin:10px auto 0;box-shadow:10px 6px 0 -2px #333}
.product-name{font-family:"Fredoka",sans-serif;font-weight:600;font-size:19px;color:var(--teal-deep);margin-top:10px}
.product-age{font-weight:600;font-size:13px;margin-top:2px}
.product-note{font-size:13.5px;line-height:16px;color:var(--muted);margin-top:10px}

/* Feedback */
.feedback{top:2222px;height:551px;background:linear-gradient(120deg,#8c9190,#c7cbca 45%,#7a7d7c)}
.feedback-title{position:absolute;left:0;width:1200px;top:100px;text-align:center;font-size:40px;color:var(--white)}
.review{position:absolute;top:179px;width:225px;height:243px;background:var(--white);border-radius:6px;text-align:center;padding:0 14px}
.review-head{font-style:italic;font-weight:600;font-size:18px;line-height:22px;color:var(--teal-deep);height:48px;display:flex;align-items:center;justify-content:center;margin-top:32px}
.review-body{font-size:12.6px;line-height:18px;color:var(--muted);margin-top:14px}
.review-name{font-weight:600;font-size:12.6px;margin-top:18px}

/* Reach */
.reach{top:2773px;height:298px;background:var(--teal)}
.reach-title{position:absolute;left:112px;top:52px;font-size:27px;color:var(--white)}
.field{position:absolute;top:98px;width:225px;height:40px;border:1px dashed rgba(255,255,255,.85);border-radius:4px;color:var(--white);font-size:15px;line-height:38px;padding-left:14px}
.submit{position:absolute;left:864px;top:98px;width:140px;height:40px;background:var(--white);border-radius:4px;color:var(--orange);font-weight:600;font-size:19px;text-align:center;line-height:40px}
.rule{position:absolute;left:112px;top:239px;width:976px;border-top:1px dashed rgba(255,255,255,.6)}
.legal{position:absolute;left:112px;top:259px;font-size:12px;color:var(--footer-ink)}
.social{position:absolute;right:110px;top:259px;display:flex;gap:12px}
.social span{width:16px;height:16px;border-radius:50%;background:var(--footer-ink)}
</style>
</head>
<body>

<section class="section hero">
  <div class="branch branch-left" role="img" aria-label="Illustrated branch with a small bird and leaves"></div>
  <div class="branch branch-right" role="img" aria-label="Illustrated branch with a small bird and leaves"></div>
  <div class="brand"><span class="brand-mark"></span><span class="brand-name">Corvane Tesk Digital</span></div>
  <nav class="nav">
    <a class="is-active" style="left:250px">Feature</a>
    <a style="left:421px">How it Work</a>
    <a style="left:592px">Product</a>
    <a style="left:763px">Testimonial</a>
    <a style="left:941px">Reach Us</a>
  </nav>
  <h1 class="heading hero-title">Simplify infant<br>sleep with AI</h1>
  <div class="hero-photo" role="img" aria-label="Smiling mother holding her baby"></div>
  <div class="hero-ring" role="img" aria-label="Hand holding the small Lunet sensor"></div>
</section>

<section class="section feature" id="feature">
  <div class="feature-photo" role="img" aria-label="Baby in a striped sleepsuit sleeping on a blue blanket"></div>
  <h2 class="heading feature-title">Feature</h2>
  <div class="feature-card" style="left:447px">
    <svg width="100" height="96" viewBox="0 0 100 96" fill="none" stroke="#56cbc4" stroke-width="6">
      <path d="M8 22V8h14M78 8h14v14M92 74v14H78M22 88H8V74"/>
      <path d="M12 48c10-16 24-24 38-24s28 8 38 24c-10 16-24 24-38 24S22 64 12 48z"/>
      <circle cx="50" cy="48" r="12" fill="#56cbc4"/>
    </svg>
    <p>Auto Tracking</p>
  </div>
  <span class="step-arrow" style="left:623px"><svg width="32" height="32" viewBox="0 0 32 32"><path d="M13 9l7 7-7 7" fill="none" stroke="#ff8029" stroke-width="2.5"/></svg></span>
  <div class="feature-card" style="left:680px">
    <svg width="100" height="96" viewBox="0 0 100 96" fill="none" stroke="#56cbc4" stroke-width="6">
      <circle cx="46" cy="52" r="38"/><circle cx="46" cy="52" r="24"/><circle cx="46" cy="52" r="9" fill="#56cbc4"/>
      <path d="M46 52L88 10M78 6l2 12 12 2"/>
    </svg>
    <p>Accurate &amp;<br>Affordable</p>
  </div>
  <span class="step-arrow" style="left:856px"><svg width="32" height="32" viewBox="0 0 32 32"><path d="M13 9l7 7-7 7" fill="none" stroke="#ff8029" stroke-width="2.5"/></svg></span>
  <div class="feature-card" style="left:915px">
    <svg width="100" height="96" viewBox="0 0 100 96" fill="none" stroke="#56cbc4" stroke-width="5">
      <path d="M54 60V22M54 36c-10 0-16-8-16-16 10 0 16 6 16 16zM54 30c0-12 8-20 18-20 0 12-8 20-18 20z"/>
      <path d="M8 70l16-12h20l14 6H40M8 70l16 14h30l34-30-8-4-22 14"/>
    </svg>
    <p>Grow with<br>the Baby</p>
  </div>
</section>

<section class="section how" id="how">
  <div class="video" role="img" aria-label="Demonstration video: the Lunet band worn on a baby's ankle">
    <svg class="play" viewBox="0 0 54 54"><circle cx="27" cy="27" r="25" fill="none" stroke="#ff8029" stroke-width="3"/><path d="M21 16l17 11-17 11z" fill="#ff8029"/></svg>
  </div>
  <h2 class="heading how-title">How it Work</h2>
  <p class="how-copy">Lunet is a soft band your baby wears while sleeping. Its sensor reads heart rate, breathing and movement, and our AI logs every nap and wake-up on your phone, with no manual entry. Watch the demo to see it in action. To order during the private launch, leave your details under Reach Us: we confirm your Lunet, take payment by card or bank transfer, and ship to your door within five days.</p>
</section>

<section class="section products" id="product">
  <h2 class="heading products-title">Product Pipeline</h2>
  <div class="product-card" style="left:188px">
    <div class="product-year">2019</div>
    <div class="product-shot" role="img" aria-label="Lilac Lunet sensor pod" style="background:#e6b3ee"></div>
    <div class="product-name">Lunet</div>
    <div class="product-age">0-1 Month</div>
    <div class="product-note">Assistant for<br>Postpartum doula</div>
  </div>
  <div class="product-card" style="left:493px">
    <div class="product-year">2020</div>
    <div class="product-shot" role="img" aria-label="White Lunet sensor pod" style="background:#f1f1f1"></div>
    <div class="product-name">Lunet +</div>
    <div class="product-age">2-18 Month</div>
    <div class="product-note">First in market,<br>Smart &amp; Affordable</div>
  </div>
  <div class="product-card" style="left:786px">
    <div class="product-year">2020</div>
    <div class="product-shot" role="img" aria-label="Mint green Lunet sensor pod" style="background:#9ee9b6"></div>
    <div class="product-name">Lunet MD</div>
    <div class="product-age">2-18 Month</div>
    <div class="product-note">Tailored for<br>Pediatricians</div>
  </div>
</section>

<section class="section feedback" id="testimonial" role="img" aria-label="Mother comforting a crying baby, black and white">
  <h2 class="heading feedback-title">Customer Feedback</h2>
  <div class="review" style="left:112px">
    <div class="review-head">I am so satisfied with this product</div>
    <p class="review-body">Lunet logs every nap for us. No more guessing at 3am, and we finally see a real sleep pattern forming.</p>
    <p class="review-name">Maren Holloway</p>
  </div>
  <div class="review" style="left:363px">
    <div class="review-head">I love It!!!!</div>
    <p class="review-body">The band is soft and our son never fusses with it. The app shows exactly when he woke and why.</p>
    <p class="review-name">Dalia Fenwick</p>
  </div>
  <div class="review" style="left:613px">
    <div class="review-head">I am so satisfied with this product</div>
    <p class="review-body">Setup took two minutes. Ordering was easy and the Lunet arrived in four days, ready to use.</p>
    <p class="review-name">Tomas Ordell</p>
  </div>
  <div class="review" style="left:865px">
    <div class="review-head">Awesome Product</div>
    <p class="review-body">Accurate, affordable and calm to use. Lunet gave two tired parents some of their sleep back.</p>
    <p class="review-name">Priya Lunden</p>
  </div>
</section>

<section class="section reach" id="reach">
  <h2 class="heading reach-title">REACH US</h2>
  <div class="field" style="left:112px">Name</div>
  <div class="field" style="left:363px">Email</div>
  <div class="field" style="left:613px">Mobile No</div>
  <div class="submit">Submit</div>
  <div class="rule"></div>
  <p class="legal">© 2019 · All rights reserved. Corvane Tesk</p>
  <div class="social" aria-label="Social links"><span></span><span></span><span></span></div>
</section>

</body>
</html>
```